Brightwater Spectral Inquiry Website

We are a paranormal research group located in Central Mississippi. We are a group dedicated to help the community in any paranormal investigation. We use fresh new techniques with cutting edge technology to investigate any paranormal situation. Our services are always free of charge to anyone. An unique feature of our group is that we provide a complete history of the property, courtesy of our research team. We would like to see designs that incorporate our logo. We are a professional group and want a professional website.. we will need a home page that will reflect out goals. Links will include "Home, About Us, Contact us, (MAYBE MORE). We will also want a "blank page" with same links that we can edit and fill in all the information..

Target Market(s)

Paranormal-Ghost hunting groups

Industry/Entity Type

Community

Coding

Coded - Design and coding required

Number of Pages Required

2 page

Font styles to use
Other font styles liked:

Requirements
Must have
• we will need a home page that will reflect out goals. Links will include "Home, About Us, Contact us, (MAYBE MORE). We will also want a "blank page" with same links that we can edit and fill in all the information..

```html
<!DOCTYPE html>
<html lang="en">
<head>
<meta charset="utf-8">
<title>Brightwater Spectral Inquiry</title>
<link rel="stylesheet" href="https://fonts.googleapis.com/css2?family=Bitter:ital,wght@0,400;0,700;1,400;1,700&family=Bangers&display=swap">
<style>
:root{
  --red:#e0151b;
  --red-dark:#b3161a;
  --yellow:#f3d418;
  --gold:#e8c21a;
  --white:#ffffff;
  --text:#e6e6e6;
  --muted:#bdbdbd;
  --black:#050505;
  --panel:#111111;
  --header:#3a3d42;
}
*{box-sizing:border-box;margin:0;padding:0}
html,body{width:904px;height:1200px;overflow:hidden;background:var(--black)}
body{position:relative;font-family:"Bitter",Georgia,serif;color:var(--text)}
.abs{position:absolute}

/* header */
.site-header{left:0;top:0;width:904px;height:144px;
  background:radial-gradient(ellipse at 45% 40%,#55595f 0%,#34373c 55%,#1d1f22 100%);
  border-top:3px solid var(--yellow)}
.brand{left:107px;top:52px;width:200px;font-size:17px;font-weight:700;color:var(--white);line-height:22px}
.util-nav{right:106px;top:12px;display:flex;gap:13px;font-size:12px}
.util-nav a{color:var(--white);text-decoration:none}
.util-nav a.current{color:var(--red)}
.follow-title{left:670px;top:51px;font-size:21px;font-style:italic;color:var(--red)}
.social{left:670px;top:85px;display:flex;gap:12px}
.social span{width:34px;height:34px;border-radius:50%;display:block;box-shadow:0 2px 3px rgba(0,0,0,.5)}
.s-blue{background:#1f5fa8}.s-cyan{background:#1aa3d4}.s-red{background:#d7262b}

/* main nav */
.main-nav{left:0;top:144px;width:904px;height:27px;background:var(--black)}
.main-nav ul{list-style:none;display:flex;position:absolute;left:107px;top:0;height:27px}
.main-nav li{font-size:13px;color:var(--white);height:27px;line-height:27px;padding:0 15px;border-left:1px solid #555}
.main-nav li:first-child{border-left:none}
.main-nav li.active{background:var(--red);padding:0 15px}
.main-nav li.active + li{border-left:none}

/* hero */
.hero{left:0;top:171px;width:904px;height:280px;
  background:radial-gradient(ellipse at 62% 45%,#8fb5a3 0%,#4d6e60 35%,#213329 75%,#131c17 100%)}
.hero-text{left:107px;top:262px;font-family:"Bangers",Impact,sans-serif;font-size:21px;letter-spacing:.5px;font-style:italic;color:var(--white);line-height:30px;text-shadow:0 1px 2px #000}
.slider-dots{left:421px;top:426px;display:flex;gap:5px}
.slider-dots span{width:12px;height:12px;border-radius:50%;background:#fff;box-shadow:0 1px 2px #000}
.slider-dots span.on{background:var(--gold)}

/* services */
.services{left:0;top:451px;width:904px;height:205px;
  background:repeating-linear-gradient(90deg,#0b0b0b 0 3px,#151515 3px 5px);border-top:1px solid #2a2a2a}
.skull{top:0;width:115px;height:205px;background:radial-gradient(ellipse at center,#3a3a3a 0%,#222 55%,rgba(20,20,20,0) 80%)}
.skull-left{left:0}.skull-right{right:0}
.services-title{left:0;top:466px;width:904px;text-align:center;font-size:26px;letter-spacing:.5px}
.services-title .r{color:var(--red)}.services-title .y{color:var(--yellow)}
.title-rule{top:482px;width:180px;height:4px;border-top:1px solid #666;border-bottom:1px solid #666}
.badges{left:0;top:0}
.badge-label{width:120px;text-align:center;font-family:"Bangers",Impact,sans-serif;font-size:21px;line-height:22px;color:var(--yellow);letter-spacing:.5px}

/* welcome */
.welcome{left:0;top:656px;width:904px;height:219px;
  background:radial-gradient(ellipse at 55% 30%,#2e2e2e 0%,#1a1a1a 60%,#0c0c0c 100%);border-top:1px solid #333}
.welcome h1{left:107px;top:673px;font-size:20px;font-style:italic;font-weight:400;color:var(--white)}
.welcome h1 em{color:var(--red)}
.welcome-rule{left:107px;top:705px;width:398px;height:4px;border-top:1px solid #777;border-bottom:1px solid #777}
.welcome-copy{left:107px;top:717px;width:398px;font-size:10.4px;font-style:italic;line-height:15px;color:var(--white);text-align:justify}
.video{left:534px;top:677px;width:264px;height:155px;background:radial-gradient(ellipse at 65% 40%,#f3d3a0 0%,#b06a24 30%,#4a2a10 70%,#1b0f06 100%)}
.video-bar{left:534px;top:832px;width:264px;height:15px;background:linear-gradient(#5b6170,#2b2f38)}

/* info columns */
.info{left:0;top:875px;width:904px;height:218px;background:repeating-linear-gradient(90deg,#0a0a0a 0 3px,#131313 3px 5px);border-top:1px solid #2a2a2a}
.col-title{top:895px;font-size:16px;color:var(--red)}
.col-rule{top:918px;width:212px;border-top:1px solid #555}
.promo{left:107px;top:934px;width:212px;height:78px;background:linear-gradient(100deg,#7b2a22 0%,#8d7a6e 45%,#5c4f45 100%)}
.col-copy{font-size:10.4px;font-style:italic;line-height:14px;color:var(--white)}
.news-date{font-size:10.5px;font-weight:700;color:var(--gold)}
.news-copy{font-size:10.4px;line-height:14px;color:var(--white);letter-spacing:.2px}
.read-more{font-size:10px;font-weight:700;color:var(--red-dark);text-align:right;width:212px}
.field{left:586px;width:212px;height:21px;background:#fff;border-radius:3px;font-size:9.5px;font-style:italic;color:#888;padding:5px 7px}
.submit{left:586px;top:1053px;width:51px;height:18px;background:var(--red-dark);border-radius:3px;color:#fff;font-size:10.5px;font-weight:700;text-align:center;line-height:18px}

/* footer */
.site-footer{left:0;top:1093px;width:904px;height:107px;background:radial-gradient(ellipse at 50% 100%,#2a2a2a 0%,#121212 60%,#070707 100%)}
.footer-links{left:0;top:1102px;width:904px;text-align:center;font-size:10.5px;color:var(--white)}
.footer-links span{color:#aaa;padding:0 4px}
.footer-social{left:414px;top:1121px;display:flex;gap:6px}
.footer-social span{width:21px;height:21px;border-radius:50%;display:block}
.footer-copy{left:115px;top:1150px;width:674px;text-align:center;font-size:8.3px;font-weight:700;line-height:11px;color:var(--muted)}
.copyright{left:0;top:1179px;width:904px;text-align:center;font-size:10.3px;color:var(--white)}
</style>
</head>
<body>

<header class="site-header abs"></header>
<div class="brand abs">Brightwater<br>Spectral Inquiry</div>
<nav class="util-nav abs"><a class="current">Case Files</a><a>Equipment</a><a>Evidence</a></nav>
<div class="follow-title abs">Follow Us</div>
<div class="social abs"><span class="s-blue"></span><span class="s-cyan"></span><span class="s-red"></span></div>

<nav class="main-nav abs">
  <ul>
    <li class="active">Home</li><li>Events &amp; Services</li><li>What we do</li><li>Meet The Team</li><li>News</li><li>Testimonials</li><li>Contact us</li>
  </ul>
</nav>

<section class="hero abs" role="img" aria-label="Night-vision photo of two investigators examining a device in a dark room"></section>
<div class="hero-text abs">WE USE FRESH NEW TECHNIQUES WITH<br>CUTTING EDGE TECHNOLOGY TO INVESTIGATE<br>ANY PARANORMAL SITUATION</div>
<div class="slider-dots abs"><span></span><span class="on"></span><span></span><span></span></div>

<section class="services abs">
  <div class="skull skull-left abs" role="img" aria-label="Faint skull decoration"></div>
  <div class="skull skull-right abs" role="img" aria-label="Faint skull decoration"></div>
</section>
<div class="title-rule abs" style="left:165px"></div>
<div class="title-rule abs" style="left:559px"></div>
<h2 class="services-title abs"><span class="r">OUR</span> <span class="y">SERVICES</span></h2>

<svg class="badges abs" width="904" height="1200" aria-hidden="true">
  <g fill="#e0151b"><circle cx="205" cy="570" r="57"/><circle cx="369" cy="570" r="57"/><circle cx="533" cy="570" r="57"/><circle cx="698" cy="570" r="57"/></g>
  <g fill="#ffffff"><circle cx="205" cy="570" r="50"/><circle cx="369" cy="570" r="50"/><circle cx="533" cy="570" r="50"/><circle cx="698" cy="570" r="50"/></g>
  <g fill="#161616"><circle cx="205" cy="570" r="47"/><circle cx="369" cy="570" r="47"/><circle cx="533" cy="570" r="47"/><circle cx="698" cy="570" r="47"/></g>
</svg>
<div class="badge-label abs" style="left:145px;top:547px">PUBLIC<br>EVENTS</div>
<div class="badge-label abs" style="left:309px;top:547px">PRIVATE<br>EVENTS</div>
<div class="badge-label abs" style="left:473px;top:547px">HAUNTED<br>PROBLEMS</div>
<div class="badge-label abs" style="left:638px;top:547px">PRIVATE<br>READINGS</div>

<section class="welcome abs" role="img" aria-label="Dark misty forest with bare trees"></section>
<h1 class="abs" style="left:107px;top:673px;font-size:20px;font-style:italic;font-weight:400;color:#fff"><em style="color:var(--red)">Welcome To</em> Brightwater Spectral Inquiry</h1>
<div class="welcome-rule abs"></div>
<p class="welcome-copy abs">Lorem ipsum dolor sit amet, consectetuer adipiscing elit, sed diam nonummy nibh euismod tincidunt ut laoreet dolore magna aliquam erat volutpat. Ut wisi enim ad minim veniam, quis nostrud exerci tation ullamcorper suscipit lobortis nisl ut aliquip ex ea commodo consequat. Duis autem vel eum iriure dolor in hendrerit in vulputate velit esse molestie consequat, vel illum dolore eu feugiat nulla facilisis at vero eros et accumsan et iusto odio dignissim qui blandit praesent luptatum Lorem ipsum dolor sit amet, consectetuer adipiscing elit, sed diam nonummy nibh zzril delenit augue duis dolore te feugait nulla facilisi.</p>
<div class="video abs" role="img" aria-label="Video still of a figure in a glowing doorway"></div>
<svg class="abs" style="left:534px;top:677px" width="264" height="170" aria-hidden="true">
  <polygon points="117,60 117,96 148,78" fill="rgba(255,255,255,.55)"/>
  <rect x="0" y="155" width="264" height="15" fill="#3a3f4a"/>
  <rect x="6" y="158" width="14" height="9" rx="2" fill="#6b8fd6"/>
  <polygon points="11,159.5 11,165.5 16,162.5" fill="#fff"/>
  <rect x="32" y="160" width="124" height="5" rx="2.5" fill="#c9ccd3"/>
  <circle cx="62" cy="162.5" r="3" fill="#fff"/>
  <text x="162" y="165" font-size="6" fill="#fff" font-family="Bitter, serif">1:47 / 12:35</text>
  <rect x="204" y="158" width="14" height="9" rx="2" fill="#6b8fd6"/>
  <rect x="223" y="158" width="15" height="9" rx="2" fill="#6b8fd6"/>
  <rect x="243" y="158" width="14" height="9" rx="2" fill="#6b8fd6"/>
</svg>

<section class="info abs"></section>
<h3 class="col-title abs" style="left:107px">Paranormal Unfiltered</h3>
<div class="col-rule abs" style="left:107px"></div>
<div class="promo abs" role="img" aria-label="Promo banner for a raw look at ghost hunting"></div>
<p class="col-copy abs" style="left:107px;top:1018px;width:212px">Lorem ipsum dolor sit amet, consectetuer adipiscing elit, sed diam nonummy nibh euismod tincidunt ut laoreet.</p>
<div class="read-more abs" style="left:107px;top:1059px">Read more »</div>

<h3 class="col-title abs" style="left:346px">News</h3>
<div class="col-rule abs" style="left:346px"></div>
<div class="news-date abs" style="left:346px;top:930px">12/NOV/2014</div>
<p class="news-copy abs" style="left:346px;top:943px;width:215px">Lorem ipsum dolor sit amet, cctetuer adipiscingin elit, sed diam nummy nibh eui smod tinciduntiot vulputate</p>
<div class="abs" style="left:346px;top:991px;width:210px;border-top:1px dashed #555"></div>
<div class="news-date abs" style="left:346px;top:996px">08/NOV/2014</div>
<p class="news-copy abs" style="left:346px;top:1010px;width:215px">Lorem ipsum dolor sit amet, cctetuer adipiscingin elit, sed diam nummy nibh eui smod tinciduntiot vulputate</p>
<div class="read-more abs" style="left:349px;top:1059px">Read more »</div>

<h3 class="col-title abs" style="left:586px">QUICK CONTACT</h3>
<div class="col-rule abs" style="left:586px"></div>
<div class="field abs" style="top:934px">Name</div>
<div class="field abs" style="top:961px">Email</div>
<div class="field abs" style="top:988px;height:53px">Message</div>
<div class="submit abs">Submit</div>

<footer class="site-footer abs" role="img" aria-label="Dim forest path fading into darkness"></footer>
<div class="footer-links abs">Home <span>|</span> Events &amp; Services <span>|</span> What we do <span>|</span> Meet The Team <span>|</span> News <span>|</span> Testimonials <span>|</span> Contact us</div>
<div class="footer-social abs"><span class="s-blue"></span><span class="s-cyan"></span><span class="s-red"></span></div>
<p class="footer-copy abs">Lorem ipsum dolor sit amet, consectetuer adipiscing elit, sed diam nonummy nibh euismod tincidunt ut laoreet dolore magna aliquam erat volutpat. Ut wisi enim ad minim veniam, quis nostrud exerci tation ullamcorper suscipit lobortis nisl</p>
<div class="copyright abs">© 2014 BrightwaterSpectralInquiry. All Rights Reserved.</div>

</body>
</html>
```